Trailbend Depot Website - Sell Outdoor product

We are a mom and pop company that just opened our website.

We need a fresh, professional, and nice looking website for our outdoor products. We sell hunting, camping, fishing, and hiking products/accessories to name a few. Some of these products are optics, gun safes, gun bi-pods and tripods, gun lights, hunting camera, tents, hearing protection, targets, fishing poles, and hiking backpacks to name a few.

Our current website is: http://www.trailbenddepot.com . You'll see our logo on the website, and it is attached. We aren't married to this logo, so if the designer thinks they can modify it or even come up with a better design for the website, they are more than welcome to do so. We need someone with good images of their own (clip art and/or outdoor images) they can use if they need to for our website.

I also attached a idea I had in visio, but please don't think this is set in stone. It is just a very rough idea. You can also go to our marketvale site to see what we sell: www.marketvale.example/shops/q7rk482mzexn3d . Right now we sell everything on Marketvale, but our website will just focus on outdoor product. So please make it an outdoor focused website. And you can be creative with some of the product category names. We also want to leave room for some parallel product in the future. Like garden tools, back yard furniture, and BBQs.

Our company also wants to include a deals section on the website. We will probably update it once a week or month. I have included what I did for a deal and accompanying images for it. Image is called Morvelik (And the main images are 01 and 02).

We also want to make sure the file is compatible with our current web-hosting company, https://www.shelfnova.example. So I included a webpage layout zip folder. If you have any questions, please contact me.

This is for a PSD and HTML/CSS webpage. If you have any artwork or images that you own and want to use them for the webpage, please do so.

Target Market(s)

The hunter, outdoors person, camper, hiker, and etc.

Industry/Entity Type

It Company

Coding

Coded - Design and coding required

Number of Pages Required

3 page

Requirements
Must have
• The main page. PSD and HTML/CSS file.
• The category page. PSD and HTML/CSS file
• The product display page. PSD and HTML/CSS file
• Please also use some images that you have or from the sites below:
• You can get free stock images for 7 days (20 per day) from this site:
• https://www.pictovault.example/complimentary/PVXKRTZ/?utm_source=PVXKFreeRT&utm_medium=cpc&utm_campaign=PVXKFreeRT&gclid=QWLp8mdTzzRBHJuBbLpeW9nKpL
• Has 14 good sites:
• http://www.venturelog.example/article/519372
• Here are the ones I like:
• https://brightfram.example/
• http://quillorbit.example/
• http://www.pagedrift.example/free/nature
• http://www.stillbarrow.example/archive
• http://tinyglints.example/
• http://vel.prkwmd.example/search/hiking
• http://fetchlumo.blogspace.example/
• http://corvelpash.example/post/584920117463/download
• http://openpixelvault.example/
• If there is a photographer listed on or next to the image, on the bottom lower corner of the image, please put the photographer's name.
Nice to have
• I would like to have an unsubscribe page. If the designer has any of their own images of the outdoor world, and they want to use them, please do. Just make the right graphic changes to make it look good.
Should not have
• Try and keep green color to a minimum.

```html
<!DOCTYPE html>
<html lang="en">
<head>
<meta charset="utf-8">
<title>Trailbend Depot</title>
<link href="https://fonts.googleapis.com/css2?family=Arimo:wght@400;700&family=Noto+Serif:ital,wght@1,400;1,700&display=swap" rel="stylesheet">
<style>
:root{
  --sky-top:#1f8fd6;
  --sky-bottom:#0a4f93;
  --red:#b0102a;
  --red-dark:#8c0a1f;
  --blue:#1b7fc4;
  --blue-dark:#0d5a9a;
  --link:#1466b0;
  --ink:#333;
  --muted:#555;
  --line:#d6d6d6;
  --white:#fff;
  --field:#0f4f85;
}
*{box-sizing:border-box;margin:0;padding:0}
html,body{width:944px;height:1200px;overflow:hidden}
body{background:linear-gradient(var(--sky-top),var(--sky-bottom));font-family:Arimo,Arial,sans-serif;color:var(--ink);position:relative}
.page{position:absolute;left:70px;top:0;width:802px;height:1200px;background:var(--white);overflow:hidden}
.abs{position:absolute}
.brand{left:18px;top:22px;display:flex;align-items:center;gap:8px;font-weight:700;font-size:24px;color:var(--red)}
.brand-mark{width:22px;height:22px;background:var(--red)}
.top-links{right:12px;top:14px;font-size:11px;color:var(--link)}
.top-links span{color:var(--muted);margin:0 5px}
.cart{left:516px;top:42px;display:flex;align-items:center;gap:6px;font-size:11.5px;font-weight:700;color:var(--link)}
.search{left:617px;top:44px;width:171px;height:23px;border:2px solid var(--red);display:flex}
.search span{flex:1;font-size:11px;padding:4px 6px;color:#444}
.search i{width:21px;background:var(--red);display:flex;align-items:center;justify-content:center}
.nav{left:13px;top:75px;width:775px;height:33px;background:var(--red);display:flex;overflow:hidden}
.nav a{flex:1 1 auto;text-align:center;color:var(--white);text-decoration:none;font-size:11px;padding:0 5px;line-height:33px;white-space:nowrap}
.nav a.active{background:var(--blue-dark)}
.hero{left:13px;top:121px;width:589px;height:261px;background:linear-gradient(#3d6b2a 0%,#5d8a3c 40%,#4a6f8d 58%,#2c4f7c 100%)}
.arrow{position:absolute;top:112px;width:36px;height:36px;border-radius:50%;background:var(--red);display:flex;align-items:center;justify-content:center}
.gift{left:615px;top:122px;width:173px;height:261px;background:linear-gradient(#fafafa,#e4e4e4);border:1px solid #d0d0d0}
.gift h2{font-family:"Noto Serif",serif;font-style:italic;font-weight:700;color:var(--blue-dark);font-size:25px;line-height:1.2;position:absolute;left:12px;top:6px}
.gift h2 span{display:block;font-size:28px}
.bow{position:absolute;right:0;top:0;width:78px;height:72px;background:var(--red);opacity:.85;border-radius:0 0 0 40px}
.select{position:absolute;left:9px;width:153px;height:24px;background:var(--white);border:1px solid #c5c5c5;font-size:11px;font-weight:700;color:var(--blue-dark);padding:5px 5px}
.select b{position:absolute;right:3px;top:3px;width:16px;height:16px;background:#c9d6e2}
.gift-btn{position:absolute;left:37px;top:222px;width:100px;height:30px;background:var(--red);border-radius:4px;color:var(--white);font-family:"Noto Serif",serif;font-style:italic;font-weight:700;font-size:14px;text-align:center;line-height:30px}
.side{left:13px;width:145px;background:linear-gradient(#fbfbfb,#ececec);border:1px solid #dcdcdc;border-radius:4px;padding:10px 10px}
.side h3{font-family:"Noto Serif",serif;font-style:italic;font-weight:700;font-size:12px;color:#333;margin-bottom:9px}
.side li{list-style:none;font-size:10px;color:#444;padding-left:11px;line-height:19px}
.side li.more{color:var(--link)}
.band{left:170px;width:618px;height:28px;background:linear-gradient(#3aa0e0,var(--blue));border-radius:4px 4px 0 0;color:var(--white);font-size:15px;padding:5px 10px}
.row{left:170px;width:618px;display:flex;justify-content:space-between}
.card{width:147px;height:184px;border:1px solid var(--line);position:relative;padding:7px 8px}
.card h4{font-size:11px;color:var(--link)}
.shot{position:absolute;left:8px;top:28px;width:130px;height:110px;background:radial-gradient(#3a3a3a,#1c1c1c 60%,#fff 72%)}
.price{position:absolute;left:7px;bottom:12px;font-size:11.5px;font-weight:700;color:var(--link)}
.buy{position:absolute;right:7px;bottom:7px;width:68px;height:21px;background:var(--red);border-radius:4px;color:var(--white);font-family:"Noto Serif",serif;font-style:italic;font-weight:700;font-size:12px;text-align:center;line-height:21px}
.footer{left:0;top:900px;width:802px;height:261px;background:var(--blue);color:var(--white)}
.fcol{position:absolute;top:20px;font-size:10px}
.fcol h5{font-size:10.5px;font-weight:700;margin-bottom:12px}
.cats li{list-style:none;border-bottom:1px solid rgba(255,255,255,.7);width:114px;line-height:20px;font-size:9.5px;white-space:nowrap}
.cats li:before{content:"» ";margin:0 4px}
.social{display:grid;grid-template-columns:22px 22px;gap:10px 8px}
.social span{width:22px;height:22px;background:rgba(255,255,255,.85);border-radius:3px}
.field{width:176px;height:23px;background:var(--field);border-radius:3px;font-size:10px;padding:6px 8px;margin-bottom:8px}
.submit{width:62px;height:23px;background:var(--red);border:1px solid #e2e2e2;font-size:11px;font-weight:700;text-align:center;line-height:21px}
.legal{left:0;top:1161px;width:802px;height:30px;background:var(--red);color:var(--white);font-size:9.5px;padding:9px 14px}
</style>
</head>
<body>
<div class="page">
  <div class="abs brand"><span class="brand-mark"></span>Trailbend Depot</div>
  <div class="abs top-links">My Account<span>|</span>Gift Certificates<span>|</span>Sign in or Create an account</div>
  <div class="abs cart">
    <svg width="24" height="22" viewBox="0 0 24 22"><path d="M1 2h4l3 11h12l3-8H7" fill="none" stroke="#333" stroke-width="2"/><circle cx="10" cy="18" r="2" fill="#333"/><circle cx="18" cy="18" r="2" fill="#333"/></svg>
    Item / $0.12
  </div>
  <div class="abs search"><span>Search</span><i><svg width="13" height="13" viewBox="0 0 13 13"><circle cx="5" cy="5" r="4" fill="none" stroke="#fff" stroke-width="2"/><path d="M8 8l4 4" stroke="#fff" stroke-width="2"/></svg></i></div>
  <nav class="abs nav">
    <a class="active">BINOCULARS</a><a>METAL DETECTORS</a><a>MICROSCOPES</a><a>RIFLESCOPES</a><a>SAFE</a><a>SHOOTING ACCESSORIES</a><a>SPOTTING SCOPES</a><a>TELESCOPES</a>
  </nav>
  <div class="abs hero" role="img" aria-label="Photo of a kayaker paddling on a lake in front of a wooded shore">
    <span class="arrow" style="left:10px"><svg width="14" height="16"><path d="M10 2L4 8l6 6" stroke="#fff" stroke-width="3" fill="none"/></svg></span>
    <span class="arrow" style="right:10px"><svg width="14" height="16"><path d="M4 2l6 6-6 6" stroke="#fff" stroke-width="3" fill="none"/></svg></span>
  </div>
  <div class="abs gift">
    <div class="bow" role="img" aria-label="Red gift ribbon bow"></div>
    <h2>GIFT<span>Finder</span></h2>
    <div class="select" style="top:121px">Category<b></b></div>
    <div class="select" style="top:153px">Products<b></b></div>
    <div class="select" style="top:185px">Price<b></b></div>
    <div class="gift-btn">Find Gifts</div>
  </div>
  <div class="abs side" style="top:396px;height:157px">
    <h3>Shop by Occasion</h3>
    <ul><li>Christmas</li><li>New Year's</li><li>Birthday</li><li>Anniversary</li><li>Bridal Shower</li><li class="more">More</li></ul>
  </div>
  <div class="abs side" style="top:566px;height:118px">
    <h3>Shop by Price</h3>
    <ul><li>Under $25</li><li>$25 - $50</li><li>$50 - $100</li><li>Over $100</li></ul>
  </div>
  <div class="abs band" style="top:396px">NEW PRODUCTS</div>
  <div class="abs row" style="top:435px">
    <div class="card"><h4>Product Name</h4><div class="shot" role="img" aria-label="Black hard-shell optics case"></div><div class="price">$60.78</div><div class="buy">Buy Now</div></div>
    <div class="card"><h4>Product Name</h4><div class="shot" role="img" aria-label="Black tactical flashlight"></div><div class="price">$41.31</div><div class="buy">Buy Now</div></div>
    <div class="card"><h4>Product Name</h4><div class="shot" role="img" aria-label="Sports watch with heart rate chest strap"></div><div class="price">$58.31</div><div class="buy">Buy Now</div></div>
    <div class="card"><h4>Product Name</h4><div class="shot" role="img" aria-label="Sport sunglasses with orange lenses"></div><div class="price">$58.31</div><div class="buy">Buy Now</div></div>
  </div>
  <div class="abs band" style="top:653px">PRODUCT LISTING</div>
  <div class="abs row" style="top:692px">
    <div class="card"><h4>Product Name</h4><div class="shot" role="img" aria-label="Black padded rifle bag"></div><div class="price">$170.00</div><div class="buy">Buy Now</div></div>
    <div class="card"><h4>Product Name</h4><div class="shot" role="img" aria-label="Black double rifle case"></div><div class="price">$116.62</div><div class="buy">Buy Now</div></div>
    <div class="card"><h4>Product Name</h4><div class="shot" role="img" aria-label="Black tactical sling backpack"></div><div class="price">$77.78</div><div class="buy">Buy Now</div></div>
    <div class="card"><h4>Product Name</h4><div class="shot" role="img" aria-label="Black tactical hiking backpack"></div><div class="price">$48.62</div><div class="buy">Buy Now</div></div>
  </div>
  <footer class="abs footer">
    <div class="fcol" style="left:16px;height:230px"><h5>Brands</h5><p>Ridgeline</p><p style="font-weight:700;margin-top:2px">View all brands</p><p style="position:absolute;top:209px;white-space:nowrap">Read More »</p></div>
    <div class="fcol cats" style="left:114px"><h5>Categories</h5><ul><li>Binoculars</li><li>Metal Detectors</li><li>microscopes</li><li>Riflescopes</li><li>Safe</li><li>Shooting accessories</li><li>Spotting Scopes</li><li>Telescopes</li><li style="font-weight:700">View all categories</li></ul></div>
    <div class="fcol" style="left:251px;width:130px"><h5>Recent Updates</h5><p style="font-size:12px;font-weight:700">Your first blog post</p><p style="font-size:9px;line-height:1.15">Welcome to your blog! A blog is a great place to share details on your ...</p><p style="margin-top:36px">Read More »</p></div>
    <div class="fcol" style="left:439px"><h5>Connect with us</h5><div class="social"><span></span><span></span><span></span><span></span></div></div>
    <div class="fcol" style="left:614px"><h5>Contact Us</h5><p style="font-weight:700;font-size:10.5px;margin:14px 0 14px">NEWSLETTER</p><div class="field">Name</div><div class="field">Email</div><div class="submit">SUBMIT</div></div>
  </footer>
  <div class="abs legal">Copyright © 2015 - All Rights Reserved - Domain Name</div>
</div>
</body>
</html>
```